Design a Homepage Mockup

We are looking to inspire a top level designer to create completely new entertaining mobile & tab friendly homepage mockup (one page only) without coding and building the website, so our in-house programmer can finish the project. We will only need templates from you to convert them to a website.
What we expect from you:
- To find an ideal balance combining good ideas from two example websites (see example websites in the wireframe Doc);
- Very soft, bright and positive colour scheme
- Large icons where mentioned in the wireframe;
- Beautiful fonts;
- Dynamic elements (e.g. five stage process with progress scale, info menu bar with some effects, pop-up menus where required);
- Try to follow menu placement idea of the Orange zone of the wireframe. All the rest of menus you can reposition as desired;
- To implement the mobile & tab friendly concept and create a separate mockup for mobile devices to see the way how the menus and bars will be repositioned when on mobile;
- We expect you to apply all your best knowledge and experience in graphic design to create a very user-friendly, entertaining, light-weight, bright, search engine friendly, mobile-friendly and dynamic homepage with soft and positive colours and beautiful fonts.
(Please find the wireframe here enclosed.)

```html
<!DOCTYPE html>
<html lang="en">
<head>
<meta charset="utf-8">
<title>Pocketly – Personalised Photo Gifts</title>
<link href="https://fonts.googleapis.com/css2?family=Dosis:wght@300;400;500;600&family=Gochi+Hand&display=swap" rel="stylesheet">
<style>
:root{
  --ink:#4a4a4a;
  --muted:#8a8a8a;
  --coral:#f47a6e;
  --red:#e8403a;
  --teal:#2f9db0;
  --teal-dark:#1f7f92;
  --sea:#7cc6c9;
  --mint:#dbe9df;
  --mint-light:#e6efe4;
  --amber:#f6b21a;
  --honey:#f3c04a;
  --honey-deep:#eaa83a;
  --line:#cfe3e6;
  --grey-bg:#efefef;
  --footer-bg:#e6e6e6;
  --white:#ffffff;
  --green:#8cc43f;
  --navy:#3b5a9a;
}
*{box-sizing:border-box;margin:0;padding:0}
html,body{width:1081px;height:1200px;overflow:hidden}
body{position:relative;background:var(--white);font-family:"Dosis",sans-serif;color:var(--ink)}
.abs{position:absolute}

/* header */
.utility{left:620px;top:4px;display:flex;gap:34px;font-size:10px;color:var(--muted)}
.utility span::before{content:"";display:inline-block;width:7px;height:7px;border:1px solid #bbb;border-radius:2px;margin-right:5px;vertical-align:-1px}
.rule-top{left:270px;top:20px;width:540px;border-top:1px dashed #d6d6d6}
.brand{left:288px;top:31px;display:flex;align-items:center;gap:3px}
.brand-dot{width:36px;height:36px;border-radius:50%;background:var(--coral)}
.brand-name{font-size:24px;font-weight:400;color:var(--ink);letter-spacing:.3px}
.main-nav{left:545px;top:22px;display:flex}
.main-nav a{width:67px;height:50px;border-left:1px solid #e4e4e4;text-decoration:none;color:var(--teal-dark);font-size:11px;display:flex;flex-direction:column;align-items:center;justify-content:flex-end;padding-bottom:6px;gap:4px}
.main-nav a svg{width:20px;height:20px}

/* hero band */
.hero-band{left:0;top:77px;width:1081px;height:587px;background:linear-gradient(180deg,var(--mint-light),var(--mint))}
.ornament{background:linear-gradient(135deg,var(--honey),var(--honey-deep))}
.ticker{left:302px;top:88px;width:508px;height:22px;background:var(--sea);color:var(--white);font-size:11.5px;display:flex;align-items:center;white-space:nowrap}
.ticker .tag{background:#9fd6d8;padding:0 6px;height:100%;display:flex;align-items:center;font-size:9px;color:#4d8f96}
.ticker .msg{flex:1;padding-left:8px;letter-spacing:.2px}
.ticker .msg b{color:var(--red);font-weight:600;font-size:13px}
.ticker .next{background:var(--teal);height:100%;padding:0 10px;display:flex;align-items:center;font-size:9px}

.promo{left:270px;width:415px;background:linear-gradient(180deg,#e8e8e6,#f5f5f3 55%,#e9e9e6);overflow:hidden}
.promo-1{top:118px;height:234px}
.promo-2{top:366px;height:283px}
.promo .title{position:absolute;text-align:center;line-height:1}
.promo .title small{display:block;font-size:19px;font-weight:400;color:var(--ink)}
.promo .title strong{display:block;font-family:"Gochi Hand",cursive;font-weight:400;color:var(--red);font-size:33px;margin-top:2px}
.promo-1 .title{left:28px;top:16px}
.promo-2 .title{right:22px;top:22px}
.promo .copy{position:absolute;left:14px;right:14px;text-align:center;font-size:10.5px;line-height:1.32;color:var(--ink)}
.promo .copy b{font-size:13px;font-weight:600}
.promo-1 .copy{top:184px}
.promo-2 .copy{top:210px}
.shop-now{left:550px;top:136px;width:64px;height:64px;border-radius:50%;background:var(--amber);color:var(--white);font-size:13px;text-align:center;line-height:1.05;display:flex;align-items:center;justify-content:center}
.photo{border-radius:6px}

.side-tiles{left:692px;top:118px;width:118px;display:flex;flex-direction:column;gap:4px}
.tile{height:55px;color:var(--white);font-size:10px;display:flex;align-items:center;justify-content:center;text-align:center;line-height:1.15;padding:0 4px}
.tile.big{font-size:11px}
.tile.t-sky{background:#7fd0dc}
.tile.t-dark{background:linear-gradient(135deg,#4b4f52,#7b7b74)}
.tile.t-navy{background:var(--navy)}
.tile.t-teal{background:#28a5c4}
.tile.t-wood{background:linear-gradient(135deg,#6e8a6a,#a86a55)}
.tile.t-aqua{background:#28b0b4}
.tile.t-green{background:var(--green);font-size:12.5px}
.tile.t-blue{background:linear-gradient(135deg,#5c6f86,#9aa7b3)}

/* steps */
.steps-line{left:270px;top:706px;width:540px;border-top:1px solid var(--line)}
.step{top:684px;width:90px;text-align:center;font-size:11px;color:var(--ink)}
.step .ring{width:44px;height:44px;margin:0 auto 18px;border-radius:50%;border:2px solid #9fd3d8;background:var(--white);display:flex;align-items:center;justify-content:center}
.step .ring svg{width:24px;height:24px}

/* reviews */
.reviews-band{left:0;top:778px;width:1081px;height:252px;background:var(--grey-bg)}
.avatar{left:270px;width:49px;height:49px}
.review{left:332px;width:352px;background:var(--white);padding:6px 10px;font-size:8.6px;line-height:1.3;color:#666}
.review::before{content:"";position:absolute;left:-7px;top:16px;border:7px solid transparent;border-left:0;border-right-color:var(--white)}
.review header{display:flex;align-items:center;font-size:10.5px;color:var(--ink);margin-bottom:4px}
.review .stars{color:var(--coral);letter-spacing:1px;font-size:8px;margin-right:12px}
.review .date{margin-left:auto;color:#aaa;font-size:8px}
.view-all{left:332px;top:1009px;font-size:9px;color:var(--ink)}
.social-title{left:706px;top:798px;font-size:12px;color:var(--ink)}
.social-title strong{font-size:16px;font-weight:500;letter-spacing:.5px}
.social-dot{left:733px;width:27px;height:27px;border-radius:50%}

/* payment + footer */
.pay-label{left:334px;top:1050px;font-size:10.5px}
.payments{left:428px;top:1043px;display:flex;gap:7px}
.payments span{height:28px;padding:0 5px;border-radius:3px;background:#f4f4f4;border:1px solid #e2e2e2;display:flex;align-items:center;font-size:9px;font-weight:600;color:var(--navy)}
.keywords{left:276px;top:1088px;width:530px;text-align:center;font-size:7.5px;line-height:1.4;color:#bbb}
.rule-bottom{left:270px;top:1120px;width:540px;border-top:1px dashed #d6d6d6}
.copyright{left:270px;top:1129px;width:540px;text-align:center;font-size:7.5px;color:#aaa}
.site-footer{left:0;top:1154px;width:1081px;height:46px;background:var(--footer-bg);display:flex;justify-content:center;align-items:center}
.site-footer a{color:#666;text-decoration:none;font-size:11px;padding:0 13px;border-left:1px solid #c8c8c8;line-height:1}
.site-footer a:first-child{border-left:0}
</style>
</head>
<body>

<!-- header -->
<nav class="abs utility"><span>Login</span><span>Sign Up</span><span>Help</span></nav>
<div class="abs rule-top"></div>
<div class="abs brand"><span class="brand-dot"></span><span class="brand-name">Pocketly</span></div>
<nav class="abs main-nav">
  <a href="#"><svg viewBox="0 0 20 20" fill="none" stroke="#f47a6e" stroke-width="1.4"><path d="M3 10 10 3l7 7M5 8.5V17h10V8.5"/><path d="M8.5 17v-4h3v4"/></svg>Home</a>
  <a href="#"><svg viewBox="0 0 20 20" fill="none" stroke="#f47a6e" stroke-width="1.4"><rect x="2.5" y="4" width="15" height="12" rx="1"/><path d="M4 14l4-4 3 3 2-2 3 3"/><circle cx="13" cy="7.5" r="1.3"/></svg>Make</a>
  <a href="#"><svg viewBox="0 0 20 20" fill="none" stroke="#f47a6e" stroke-width="1.4"><path d="M4 17 13 8M11 4v3M15 5l-2 2M16 9h-3"/></svg>Occasions</a>
  <a href="#"><svg viewBox="0 0 20 20" fill="none" stroke="#f47a6e" stroke-width="1.4"><rect x="4" y="7" width="12" height="10" rx="1"/><path d="M7 7V5a3 3 0 0 1 6 0v2"/></svg>Basket</a>
</nav>

<!-- hero band -->
<div class="abs hero-band" role="img" aria-label="Soft mint background with a light repeating leaf pattern"></div>
<div class="abs ornament" role="img" aria-label="Honeycomb patterned gift tag ornament with a ribbon bow and dotted trail" style="left:178px;top:130px;width:92px;height:136px"></div>
<div class="abs ornament" role="img" aria-label="Honeycomb patterned ornament" style="left:332px;top:77px;width:72px;height:10px"></div>
<div class="abs ornament" role="img" aria-label="Honeycomb patterned ornament with dotted trail" style="left:823px;top:597px;width:111px;height:67px"></div>

<div class="abs ticker"><span class="tag">New ›</span><span class="msg">MID SEASON SALE NOW ON! FURTHER REDUCTIONS ON ALL NOTEBOOKS - SAVE UP TO <b>20%</b></span><span class="next">Next ›</span></div>

<section class="abs promo promo-1">
  <h2 class="title"><small>photo travel card</small><strong>Holders</strong></h2>
  <div class="abs photo" role="img" aria-label="Photo card holder showing a smiling child" style="left:150px;top:48px;width:84px;height:112px;background:linear-gradient(160deg,#9cc46a,#e5c9a4 55%,#c7a07a);transform:rotate(-6deg)"></div>
  <div class="abs photo" role="img" aria-label="Photo card holder showing a couple outdoors" style="left:240px;top:84px;width:108px;height:80px;background:linear-gradient(160deg,#7fb8d8,#d9c6ae 60%,#7c9aab);transform:rotate(6deg)"></div>
  <p class="copy">Pocketly lets you design your own unique travel card wallet online in just a few minutes!<br>We allow you to upload your favourite photos and personalise the caption to get your special travel card holder printed and posted direct or back to you. <b>From only £4.99</b></p>
</section>
<div class="abs shop-now">SHOP<br>NOW</div>

<section class="abs promo promo-2">
  <h2 class="title"><small>personalised photo</small><strong>Notebooks</strong></h2>
  <div class="abs photo" role="img" aria-label="Photo notebook cover showing a woman reading on a bench" style="left:34px;top:20px;width:104px;height:166px;background:linear-gradient(170deg,#c9b89c,#d88f86 50%,#8d7a68)"></div>
  <div class="abs" role="img" aria-label="Open blank notebook" style="left:150px;top:114px;width:170px;height:82px;background:linear-gradient(180deg,#fbfbf9,#dcdcd6);transform:skewX(-12deg)"></div>
  <p class="copy">Personalised photo notebook can become either an individual accessory for yourself or a thoughtful gift for your relatives, loved ones, friends or colleagues. «Pocketlys» will make it easy and fascinating for you to create your own custom photo notebook and to expand the opportunities to showcase your exciting and original ideas, illustrating those precious treasured moments of your life. <b>From only £7.99</b></p>
</section>

<aside class="abs side-tiles">
  <div class="tile t-sky big">FATHER'S DAY<br>15th June</div>
  <div class="tile t-dark" role="img" aria-label="Computer desk photo">Upload pictures<br>from your computer</div>
  <div class="tile t-navy big">Connect to Your<br>Friendbook<br>Albums!</div>
  <div class="tile t-dark" role="img" aria-label="Phone with photos">Connect to your<br>Snapgram<br>account to customise!</div>
  <div class="tile t-teal big">24h<br>Despatch on all Travel<br>Card Holders</div>
  <div class="tile t-wood" role="img" aria-label="Row of colourful notebooks">Choose From Tens<br>of Layouts</div>
  <div class="tile t-aqua big">Quick &amp; Easy Five-Stage<br>Process</div>
  <div class="tile t-green">Free UK Shipping</div>
  <div class="tile t-blue" role="img" aria-label="Verified payment photo">PayWell Verified</div>
</aside>

<!-- steps -->
<div class="abs steps-line"></div>
<div class="abs step" style="left:276px"><div class="ring"><svg viewBox="0 0 24 24" fill="none" stroke="#2f9db0" stroke-width="1.5"><path d="M10 20v-9a1.5 1.5 0 0 1 3 0v4l4 1v4"/><circle cx="11.5" cy="6" r="3"/></svg></div>1. Select</div>
<div class="abs step" style="left:385px"><div class="ring"><svg viewBox="0 0 24 24" fill="none" stroke="#2f9db0" stroke-width="1.5"><path d="M5 5l14 14M19 5 5 19"/></svg></div>2. Personalise</div>
<div class="abs step" style="left:495px"><div class="ring"><svg viewBox="0 0 24 24" fill="none" stroke="#2f9db0" stroke-width="1.5"><circle cx="12" cy="12" r="8"/><path d="M8 12l3 3 7-8"/></svg></div>3. Review</div>
<div class="abs step" style="left:604px"><div class="ring"><svg viewBox="0 0 24 24" fill="none" stroke="#2f9db0" stroke-width="1.5"><path d="M4 10h16l-2 9H6zM8 10l4-5 4 5M9 13v3M12 13v3M15 13v3"/></svg></div>4. Basket</div>
<div class="abs step" style="left:712px"><div class="ring" style="color:#2f9db0;font-size:22px">£</div>5. Checkout</div>

<!-- reviews -->
<div class="abs reviews-band"></div>
<div class="abs avatar" role="img" aria-label="Customer portrait" style="top:798px;background:linear-gradient(135deg,#5b3a2e,#c79a84)"></div>
<div class="abs avatar" role="img" aria-label="Customer portrait" style="top:862px;background:linear-gradient(135deg,#3d7a8a,#a07a5c)"></div>
<div class="abs avatar" role="img" aria-label="Customer portrait" style="top:924px;background:linear-gradient(135deg,#3a2c26,#b58a70)"></div>

<article class="abs review" style="top:798px;height:52px"><header><span class="stars">★★★★★</span>Clara,<span class="date">◷ 14-06-2015</span></header>5 star product and service. Product was excellent and I am in the process of buying some more and the delivery was next day. I wouldn't hesitate to recommend Pocketly.</article>
<article class="abs review" style="top:862px;height:52px"><header><span class="stars">★★★★★</span>J Porter,<span class="date">◷ 01-06-2015</span></header>Simple and effective! The online interface is so easy to use, I paid instantly, and my new wallet arrived later that week. It was fast, simple and I couldn't ask for more. Great service.</article>
<article class="abs review" style="top:924px;height:78px"><header><span class="stars">★★★★★</span>Gavin,<span class="date">◷ 19-05-2015</span></header>Fantastic personalised Ripple Card holders! Go to their website, upload your photo(s), resize and position and save. You have created your own unique holder for your Ripple Card or other credit card sized item. The quality is excellent, postage is FREE and the turnaround is TWO days! Cannot recommend more highly. They really make great, unusual gifts.</article>
<div class="abs view-all">View all ▾</div>

<div class="abs social-title">Let's Get <strong>Social</strong></div>
<span class="abs social-dot" style="top:825px;background:#3b5a9a"></span>
<span class="abs social-dot" style="top:855px;background:#29b4e8"></span>
<span class="abs social-dot" style="top:884px;background:#e9593f"></span>
<span class="abs social-dot" style="top:913px;background:#6b5448"></span>
<span class="abs social-dot" style="top:943px;background:#e8514a"></span>
<span class="abs social-dot" style="top:973px;background:#e8403a"></span>

<!-- payments + footer -->
<div class="abs pay-label">Payment methods</div>
<div class="abs payments"><span>PayWell</span><span>MeritCard</span><span>Versa</span><span>Mondo</span><span>Apex Express</span></div>
<p class="abs keywords">Personalised photo notebooks, individual accessory, save moments of your life, photo travel card holders, pocketly, delivery next day, special travel card, free UK shipping, fast, cool, free</p>
<div class="abs rule-bottom"></div>
<p class="abs copyright">© Pocketly Limited 2015</p>
<footer class="abs site-footer"><a href="#">Terms and Conditions</a><a href="#">Privacy Policy</a><a href="#">Contact Us</a><a href="#">Blog</a><a href="#">Large Orders</a></footer>

</body>
</html>
```